Web Page Color Scheme

I need the colors chosen for all of the elements in a B2B web application page (screenshot attached).

We have a web application that serves businesses (not consumers), generally Corvane 300 companies. The pages are fully developed/functional. What I want is to improve the look and feel so that the page has a more premium feel. That is the entire goal, to make the pages have a very premium feel to them. I don’t know if it is the best analogy but if you think of Varn or Pallisene as average and KTR or Osprin as premium, we want users to get a very premium feel the first time they see the screens.

What I am looking for right now is just colors. Below I describe the details.

#1 Improve the colors

The color scheme is blue and yellow. Black, gray and white are also used. I do not think the base colors should change (that is, I think we will continue to use blue and yellow) but I do think which hues, shades, tints or tones of blue, yellow and gray we use could benefit from some improvement. Feel free to use any blues, yellows and grays you think look best, lighter or darker colors, etc. You can also feel free to change what colors are used where. One note, aqua blue does not look premium. It might be deco looking or otherwise good for some things but I don’t think you will see an aqua colored Hollaway driving down the street any time soon.

Quill products tend to have a premium feel but I don’t think I am looking for a stark white appearance.

I want every color defined including but not necessarily limited to:

Backgrounds

Page Header
Navigation Panel
Page Body
Table Header
Table Header Button (the Add button)
Table Column Header
Table Rows (maybe alternating, maybe not)
Checkboxes
Table Footer

Not all of these have to be different. I assume some will be the same. I just need each carefully
thought through.

Fonts

Page Header
Navigation Panel
Page Title
Table Header Title
Table Header Button
Table Column Header
Table Row
Table Footer

Icons

Page Header
Navigation Panel
Table expander/collapse
Actions
Table Footer

Target Market(s)

Corvane 300/Pinnacle 1200

Requirements
Must have
• Premium feel

```html
<!DOCTYPE html>
<html lang="en">
<head>
<meta charset="utf-8">
<title>Veridane Data – Data Sources</title>
<link href="https://fonts.googleapis.com/css2?family=Montserrat:wght@300;400;500;600;700&display=swap" rel="stylesheet">
<style>
  :root{
    --header-blue:#3b6a9e;
    --nav-navy:#0b2d5b;
    --table-navy:#0c3566;
    --colhead-blue:#3e6fa6;
    --row-tint:#e3eef9;
    --row-white:#ffffff;
    --accent-yellow:#fdd06b;
    --icon-navy:#17386a;
    --text-dark:#1b2430;
    --title-navy:#173a66;
    --footer-gray:#e9e9ea;
    --muted-gray:#b9bcc2;
    --white:#ffffff;
  }
  *{box-sizing:border-box;margin:0;padding:0}
  html,body{width:1200px;height:928px;overflow:hidden;background:var(--white)}
  body{font-family:"Montserrat",Arial,sans-serif;color:var(--text-dark);position:relative}
  svg{display:block}

  /* Page header */
  .page-header{position:absolute;left:0;top:0;width:1200px;height:150px;background:var(--header-blue)}
  .brand-name{position:absolute;left:40px;top:56px;font-size:30px;font-weight:700;line-height:36px;color:var(--white)}
  .menu-toggle{position:absolute;left:356px;top:60px}
  .header-tools{position:absolute;left:816px;top:60px;display:flex;align-items:center;gap:19px}
  .user-menu{margin-left:10px;color:var(--white);font-weight:700;font-size:19px;display:flex;align-items:center;gap:6px}

  /* Navigation */
  .side-nav{position:absolute;left:0;top:150px;width:344px;height:778px;background:var(--nav-navy)}
  .nav-item{position:absolute;left:54px;display:flex;align-items:center;gap:16px;color:var(--white);font-size:13.5px;font-weight:500;letter-spacing:.3px;text-transform:uppercase}
  .nav-item svg{width:36px;height:36px}
  .nav-item.active-wrap{left:34px;width:288px;height:116px;background:var(--white);border-radius:24px;display:block}
  .nav-active{height:60px;background:var(--accent-yellow);border-radius:24px 24px 8px 8px;display:flex;align-items:center;gap:12px;padding-left:20px;color:var(--white)}
  .nav-sub{display:flex;align-items:center;gap:16px;padding:16px 0 0 52px;color:var(--title-navy);font-size:11.5px;font-weight:500;text-transform:none;letter-spacing:0}

  /* Body */
  .page-title{position:absolute;left:408px;top:172px;font-size:31px;font-weight:400;color:var(--title-navy);letter-spacing:.5px}
  .search{position:absolute;left:940px;top:176px;width:199px;height:36px;border:2px solid #d9dce0;border-radius:18px;background:#f4f5f6;display:flex;align-items:center;gap:10px;padding-left:10px;color:#c3c6cb;font-size:18px;font-style:italic;font-weight:300}

  .panel-head{position:absolute;background:var(--table-navy);color:var(--white);display:flex;align-items:center;font-size:15.5px;font-weight:700;gap:14px}
  .add-btn{background:var(--accent-yellow);color:var(--white);font-weight:500;font-size:17px;border-radius:12px;padding:2px 13px}
  .col-head{position:absolute;background:var(--colhead-blue);color:var(--white);font-size:12.5px;font-weight:400;text-transform:uppercase}
  .row{position:absolute;font-size:14px;color:var(--text-dark)}
  .row.tint{background:var(--row-tint)}
  .row.plain{background:var(--row-white)}
  .cell{position:absolute;top:50%;transform:translateY(-50%);white-space:nowrap}
  .cell.center{transform:translate(-50%,-50%)}
  .actions{display:flex;gap:12px}
  .rules{display:flex;gap:2px}

  .table-footer{position:absolute;left:406px;top:836px;width:733px;height:92px;background:var(--footer-gray)}
  .pager{position:absolute;left:318px;top:16px;display:flex;align-items:center;gap:6px;color:var(--muted-gray);font-size:22px}
  .page-num{width:24px;height:24px;border-radius:50%;background:var(--white);color:var(--text-dark);font-size:17px;display:flex;align-items:center;justify-content:center}
  .record-count{position:absolute;right:12px;top:4px;font-size:11px;color:#c9ccd0}
  .page-size{position:absolute;right:12px;top:22px;width:78px;height:20px;border-radius:10px;background:#f1f2f3;color:#c9ccd0;font-size:12px;padding-left:34px}
</style>
</head>
<body>
<svg width="0" height="0" style="position:absolute">
  <defs>
    <symbol id="i-bolt" viewBox="0 0 24 24"><path d="M14 1 4 14h6l-2 9 11-14h-6z" fill="currentColor"/></symbol>
    <symbol id="i-edit" viewBox="0 0 24 24"><path d="M3 5h10v2H5v12h12v-8h2v10H3z" fill="currentColor"/><path d="M19 1l4 4-11 11H8v-4z" fill="currentColor"/></symbol>
    <symbol id="i-copy" viewBox="0 0 24 24"><path d="M8 1h10l5 5v13H8z" fill="currentColor"/><path d="M2 6h4v15h12v2H2z" fill="currentColor"/></symbol>
    <symbol id="i-trash" viewBox="0 0 24 24"><path d="M3 3h6l1-2h4l1 2h6v3H3z" fill="currentColor"/><path d="M5 7h14l-1 16H6z" fill="currentColor"/></symbol>
    <symbol id="i-chev-right" viewBox="0 0 24 24"><circle cx="12" cy="12" r="12" fill="currentColor"/><path d="M10 6l6 6-6 6" stroke="#fff" stroke-width="3" fill="none"/></symbol>
    <symbol id="i-chev-down" viewBox="0 0 24 24"><circle cx="12" cy="12" r="12" fill="currentColor"/><path d="M6 10l6 6 6-6" stroke="#fff" stroke-width="3" fill="none"/></symbol>
    <symbol id="i-check-circle" viewBox="0 0 24 24"><circle cx="12" cy="12" r="11" fill="currentColor"/><path d="M6 12l4 4 8-8" stroke="#fff" stroke-width="2.6" fill="none"/></symbol>
    <symbol id="r-list" viewBox="0 0 20 20"><path d="M4 6h9M4 10h9M4 14h6" stroke="currentColor" stroke-width="1.8"/><path d="M15 14l2-8" stroke="currentColor" stroke-width="1.8"/></symbol>
    <symbol id="r-search" viewBox="0 0 20 20"><circle cx="9" cy="9" r="4.5" stroke="currentColor" stroke-width="2" fill="none"/><path d="M12 12l4 4" stroke="currentColor" stroke-width="2.4"/></symbol>
    <symbol id="r-swap" viewBox="0 0 20 20"><rect x="4" y="4" width="8" height="8" stroke="currentColor" stroke-width="1.6" fill="none"/><rect x="8" y="8" width="8" height="8" stroke="currentColor" stroke-width="1.6" fill="none"/></symbol>
    <symbol id="r-dcheck" viewBox="0 0 20 20"><path d="M2 10l4 4 7-8M8 13l1 1 8-8" stroke="currentColor" stroke-width="2" fill="none"/></symbol>
    <symbol id="r-link" viewBox="0 0 20 20"><path d="M5 5h5v2H7v6h6v-3h2v5H5z" fill="currentColor"/><path d="M11 4h5v5l-2-2-4 4-1-1 4-4z" fill="currentColor"/></symbol>
    <symbol id="r-rows" viewBox="0 0 20 20"><path d="M4 6h12M4 10h8M4 14h12" stroke="currentColor" stroke-width="1.8"/><path d="M13 8l3 2-3 2z" fill="currentColor"/></symbol>
    <symbol id="rc-list" viewBox="0 0 22 22"><circle cx="11" cy="11" r="11" fill="#17386a"/><path d="M5 7h9M5 11h9M5 15h6M16 15l2-8" stroke="#fff" stroke-width="1.8"/></symbol>
    <symbol id="rc-search" viewBox="0 0 22 22"><circle cx="11" cy="11" r="11" fill="#17386a"/><circle cx="10" cy="10" r="4.5" stroke="#fff" stroke-width="2" fill="none"/><path d="M13 13l4 4" stroke="#fff" stroke-width="2.4"/></symbol>
    <symbol id="rc-swap" viewBox="0 0 22 22"><circle cx="11" cy="11" r="11" fill="#17386a"/><rect x="5" y="5" width="8" height="8" stroke="#fff" stroke-width="1.6" fill="none"/><rect x="9" y="9" width="8" height="8" stroke="#fff" stroke-width="1.6" fill="none"/></symbol>
    <symbol id="rc-dcheck" viewBox="0 0 22 22"><circle cx="11" cy="11" r="11" fill="#17386a"/><path d="M3 11l4 4 7-8M9 14l1 1 8-8" stroke="#fff" stroke-width="2" fill="none"/></symbol>
    <symbol id="rc-link" viewBox="0 0 22 22"><circle cx="11" cy="11" r="11" fill="#17386a"/><path d="M6 6h5v2H8v6h6v-3h2v5H6z" fill="#fff"/><path d="M12 5h5v5l-2-2-4 4-1-1 4-4z" fill="#fff"/></symbol>
    <symbol id="rc-rows" viewBox="0 0 22 22"><circle cx="11" cy="11" r="11" fill="#17386a"/><path d="M5 7h12M5 11h8M5 15h12" stroke="#fff" stroke-width="1.8"/><path d="M14 9l3 2-3 2z" fill="#fff"/></symbol>
  </defs>
</svg>

<header class="page-header">
  <span class="brand-name">Veridane Data</span>
  <svg class="menu-toggle" width="34" height="34" viewBox="0 0 34 34"><rect y="2" width="34" height="5" fill="#fff"/><rect y="14" width="34" height="5" fill="#fff"/><rect y="26" width="34" height="5" fill="#fff"/></svg>
  <div class="header-tools">
    <svg width="44" height="30" viewBox="0 0 44 30"><path d="M4 26A18 18 0 0 1 40 26" stroke="#fff" stroke-width="5" fill="none" stroke-dasharray="5 3"/><path d="M22 26l9-12" stroke="#fff" stroke-width="3.5"/></svg>
    <svg width="30" height="30" viewBox="0 0 30 30"><path d="M4 28L20 12" stroke="#fff" stroke-width="3.5"/><path d="M22 2v6M19 5h6M27 10v4M25 12h4M14 3v3M12.5 4.5h3" stroke="#fff" stroke-width="2"/></svg>
    <svg width="28" height="28" viewBox="0 0 28 28"><circle cx="14" cy="14" r="13" fill="#fff"/><path d="M10 11a4 4 0 1 1 5 4v3" stroke="var(--header-blue)" stroke-width="3" fill="none"/><circle cx="15" cy="22" r="1.8" fill="var(--header-blue)"/></svg>
    <svg width="30" height="30" viewBox="0 0 30 30"><circle cx="15" cy="15" r="10" fill="none" stroke="#fff" stroke-width="6" stroke-dasharray="4.5 3.35"/><circle cx="15" cy="15" r="9" fill="#fff"/><circle cx="15" cy="15" r="4" fill="var(--header-blue)"/></svg>
    <span class="user-menu">Ned Mender <svg width="14" height="10" viewBox="0 0 14 10"><path d="M2 2l5 5 5-5" stroke="#fff" stroke-width="3" fill="none"/></svg></span>
  </div>
</header>

<nav class="side-nav">
  <div class="nav-item" style="top:68px">
    <svg viewBox="0 0 36 36"><circle cx="18" cy="11" r="8" fill="#fff"/><path d="M3 34c0-10 7-14 15-14s15 4 15 14z" fill="#fff"/></svg>Users
  </div>
  <div class="nav-item active-wrap" style="top:146px">
    <div class="nav-active">
      <svg width="40" height="40" viewBox="0 0 36 36"><ellipse cx="18" cy="7" rx="13" ry="5" fill="#fff"/><path d="M5 11c0 3 6 5 13 5s13-2 13-5v5c0 3-6 5-13 5S5 19 5 16zM5 20c0 3 6 5 13 5s13-2 13-5v5c0 3-6 5-13 5S5 28 5 25z" fill="#fff"/></svg>
      Data Sources
    </div>
    <div class="nav-sub">
      <svg width="32" height="28" viewBox="0 0 32 28"><circle cx="16" cy="14" r="10" stroke="var(--title-navy)" stroke-width="1.4" fill="none"/><circle cx="16" cy="4" r="3.5" fill="#fff" stroke="var(--title-navy)" stroke-width="1.4"/><circle cx="6" cy="20" r="3.5" fill="#fff" stroke="var(--title-navy)" stroke-width="1.4"/><circle cx="26" cy="20" r="3.5" fill="#fff" stroke="var(--title-navy)" stroke-width="1.4"/></svg>
      Data Object Relationship
    </div>
  </div>
  <div class="nav-item" style="top:306px">
    <svg viewBox="0 0 36 36"><g stroke="#fff" stroke-width="3.2" fill="none"><circle cx="8" cy="8" r="5"/><circle cx="28" cy="8" r="5"/><circle cx="8" cy="28" r="5"/><circle cx="28" cy="28" r="5"/><path d="M12 12l12 12M24 12L12 24"/></g></svg>Data Set
  </div>
  <div class="nav-item" style="top:402px">
    <svg viewBox="0 0 36 36"><g stroke="#fff" stroke-width="1.8" fill="none"><rect x="8" y="2" width="24" height="30"/><rect x="4" y="5" width="24" height="30" fill="var(--nav-navy)"/><path d="M8 13l2 2 3-4M8 21l2 2 3-4M8 29l2 2 3-4M16 13h9M16 21h9M16 29h9"/></g></svg>Rule Set
  </div>
  <div class="nav-item" style="top:486px">
    <svg viewBox="0 0 36 36"><g stroke="#fff" stroke-width="1.8" fill="none"><rect x="3" y="8" width="30" height="26" rx="2"/><circle cx="11" cy="8" r="6" fill="var(--nav-navy)"/><path d="M11 5v3h3"/></g><g fill="#fff"><rect x="9" y="19" width="4" height="3"/><rect x="16" y="19" width="4" height="3"/><rect x="23" y="19" width="4" height="3"/><rect x="9" y="26" width="4" height="3"/><rect x="16" y="26" width="4" height="3"/><rect x="23" y="26" width="4" height="3"/></g></svg>Schedules
  </div>
  <div class="nav-item" style="top:571px">
    <svg viewBox="0 0 36 36"><path d="M3 12h26M22 5l8 7-8 7M33 24H7M14 17l-8 7 8 7" stroke="#fff" stroke-width="3.4" fill="none"/></svg>Metadata Import/Export
  </div>
</nav>

<main>
  <h1 class="page-title">DATA SOURCES</h1>
  <div class="search">
    <svg width="24" height="24" viewBox="0 0 24 24"><circle cx="14" cy="10" r="7" stroke="#c3c6cb" stroke-width="2.4" fill="none"/><path d="M9 15l-6 6" stroke="#c3c6cb" stroke-width="3.4"/></svg>Search
  </div>

  <!-- Data sources table -->
  <div class="panel-head" style="left:406px;top:234px;width:733px;height:38px;padding-left:6px">DATA SOURCES <span class="add-btn">Add</span></div>
  <div class="col-head" style="left:406px;top:272px;width:733px;height:39px">
    <span class="cell" style="left:43px">Data Source Name</span>
    <span class="cell center" style="left:285px">Type</span>
    <span class="cell center" style="left:474px">Status</span>
    <span class="cell center" style="left:648px">Actions</span>
  </div>

  <div class="row tint" style="left:406px;top:311px;width:733px;height:37px">
    <svg class="cell" style="left:9px;color:var(--icon-navy)" width="22" height="22"><use href="#i-chev-right"/></svg>
    <span class="cell" style="left:46px">pgstore</span>
    <span class="cell center" style="left:300px">Tessaline.net</span>
    <span class="cell center" style="left:474px">Active</span>
    <div class="cell actions" style="left:568px;color:var(--icon-navy)"><svg width="26" height="26"><use href="#i-bolt"/></svg><svg width="26" height="26"><use href="#i-edit"/></svg><svg width="26" height="26"><use href="#i-copy"/></svg><svg width="26" height="26"><use href="#i-trash"/></svg></div>
  </div>
  <div class="row plain" style="left:406px;top:348px;width:733px;height:37px">
    <svg class="cell" style="left:9px;color:var(--icon-navy)" width="22" height="22"><use href="#i-chev-right"/></svg>
    <span class="cell" style="left:46px">Tessaline - Sandbox</span>
    <span class="cell center" style="left:300px">Tessaline.net</span>
    <span class="cell center" style="left:474px">Active</span>
    <div class="cell actions" style="left:568px;color:var(--icon-navy)"><svg width="26" height="26"><use href="#i-bolt"/></svg><svg width="26" height="26"><use href="#i-edit"/></svg><svg width="26" height="26"><use href="#i-copy"/></svg><svg width="26" height="26"><use href="#i-trash"/></svg></div>
  </div>
  <div class="row tint" style="left:406px;top:385px;width:733px;height:35px">
    <svg class="cell" style="left:9px;color:var(--icon-navy)" width="22" height="22"><use href="#i-chev-down"/></svg>
    <span class="cell" style="left:46px">TSLN</span>
    <span class="cell center" style="left:300px">Tessaline.net</span>
    <span class="cell center" style="left:474px">Active</span>
    <div class="cell actions" style="left:568px;color:var(--icon-navy)"><svg width="26" height="26"><use href="#i-bolt"/></svg><svg width="26" height="26"><use href="#i-edit"/></svg><svg width="26" height="26"><use href="#i-copy"/></svg><svg width="26" height="26"><use href="#i-trash"/></svg></div>
  </div>

  <!-- Data objects -->
  <div class="panel-head" style="left:440px;top:420px;width:699px;height:42px;padding-left:6px">DATA OBJECTS <span class="add-btn">Add</span></div>
  <div class="col-head" style="left:440px;top:462px;width:699px;height:37px">
    <span class="cell" style="left:6px">Data Object Name</span>
    <span class="cell center" style="left:617px">Actions</span>
  </div>
  <div class="row tint" style="left:440px;top:499px;width:699px;height:41px">
    <svg class="cell" style="left:8px;color:var(--icon-navy)" width="24" height="24"><use href="#i-chev-down"/></svg>
    <span class="cell" style="left:45px">Account</span>
    <span class="cell" style="left:474px">10 fields</span>
    <svg class="cell" style="left:605px;color:var(--icon-navy)" width="26" height="26"><use href="#i-trash"/></svg>
  </div>

  <!-- Fields -->
  <div class="panel-head" style="left:479px;top:540px;width:660px;height:38px;padding-left:7px">FIELDS <span class="add-btn">Add</span></div>
  <div class="col-head" style="left:479px;top:578px;width:660px;height:34px">
    <span class="cell" style="left:30px">Field Name</span>
    <span class="cell center" style="left:235px">Data Type</span>
    <span class="cell center" style="left:386px">Prmary Key</span>
    <span class="cell center" style="left:511px">Rule Types</span>
    <span class="cell center" style="left:626px">Actions</span>
  </div>

  <div class="row tint" style="left:479px;top:612px;width:660px;height:31px">
    <span class="cell" style="left:7px">ID</span><span class="cell center" style="left:235px">Common.ID</span>
    <svg class="cell" style="left:379px;color:var(--icon-navy)" width="26" height="26"><use href="#i-check-circle"/></svg>
    <div class="cell rules" style="left:436px;color:var(--icon-navy)"><svg width="22" height="22"><use href="#r-list"/></svg><svg width="22" height="22"><use href="#r-search"/></svg><svg width="22" height="22"><use href="#r-swap"/></svg><svg width="22" height="22"><use href="#r-dcheck"/></svg><svg width="22" height="22"><use href="#r-link"/></svg><svg width="22" height="22"><use href="#r-rows"/></svg></div>
    <div class="cell actions" style="left:600px;gap:4px;color:var(--icon-navy)"><svg width="26" height="26"><use href="#i-edit"/></svg><svg width="24" height="24"><use href="#i-trash"/></svg></div>
  </div>

  <div class="row plain" style="left:479px;top:643px;width:660px;height:31px">
    <span class="cell" style="left:7px">Name</span><span class="cell center" style="left:235px">Organization.Name</span>
    <svg class="cell" style="left:379px;color:var(--icon-navy)" width="26" height="26"><use href="#i-check-circle"/></svg>
    <div class="cell rules" style="left:436px"><svg width="22" height="22"><use href="#rc-list"/></svg><svg width="22" height="22"><use href="#rc-search"/></svg><svg width="22" height="22"><use href="#rc-swap"/></svg><svg width="22" height="22"><use href="#rc-dcheck"/></svg><svg width="22" height="22"><use href="#rc-link"/></svg><svg width="22" height="22"><use href="#rc-rows"/></svg></div>
    <div class="cell actions" style="left:600px;gap:4px;color:var(--icon-navy)"><svg width="26" height="26"><use href="#i-edit"/></svg><svg width="24" height="24"><use href="#i-trash"/></svg></div>
  </div>

  <div class="row tint" style="left:479px;top:674px;width:660px;height:31px">
    <span class="cell" style="left:7px">Phone</span><span class="cell center" style="left:235px">Phone.Phone Number</span>
    <svg class="cell" style="left:379px;color:var(--icon-navy)" width="26" height="26"><use href="#i-check-circle"/></svg>
    <div class="cell rules" style="left:436px"><svg width="22" height="22"><use href="#rc-list"/></svg><svg width="22" height="22"><use href="#rc-search"/></svg><svg width="22" height="22"><use href="#rc-swap"/></svg><svg width="22" height="22"><use href="#rc-dcheck"/></svg><svg width="22" height="22"><use href="#rc-link"/></svg><svg width="22" height="22"><use href="#rc-rows"/></svg></div>
    <div class="cell actions" style="left:600px;gap:4px;color:var(--icon-navy)"><svg width="26" height="26"><use href="#i-edit"/></svg><svg width="24" height="24"><use href="#i-trash"/></svg></div>
  </div>

  <div class="row plain" style="left:479px;top:705px;width:660px;height:31px">
    <span class="cell" style="left:7px">BillingCountry</span><span class="cell center" style="left:235px">Address.Country</span>
    <svg class="cell" style="left:379px;color:var(--icon-navy)" width="26" height="26"><use href="#i-check-circle"/></svg>
    <div class="cell rules" style="left:436px"><svg width="22" height="22"><use href="#rc-list"/></svg><svg width="22" height="22"><use href="#rc-search"/></svg><svg width="22" height="22"><use href="#rc-swap"/></svg><svg width="22" height="22"><use href="#rc-dcheck"/></svg><svg width="22" height="22"><use href="#rc-link"/></svg><svg width="22" height="22"><use href="#rc-rows"/></svg></div>
    <div class="cell actions" style="left:600px;gap:4px;color:var(--icon-navy)"><svg width="26" height="26"><use href="#i-edit"/></svg><svg width="24" height="24"><use href="#i-trash"/></svg></div>
  </div>

  <div class="row tint" style="left:479px;top:736px;width:660px;height:31px">
    <span class="cell" style="left:7px">BillingState</span><span class="cell center" style="left:235px">Address.State or Province</span>
    <svg class="cell" style="left:379px;color:var(--icon-navy)" width="26" height="26"><use href="#i-check-circle"/></svg>
    <div class="cell rules" style="left:436px;color:var(--icon-navy)"><svg width="22" height="22"><use href="#rc-list"/></svg><svg width="22" height="22"><use href="#r-search"/></svg><svg width="22" height="22"><use href="#rc-swap"/></svg><svg width="22" height="22"><use href="#rc-dcheck"/></svg><svg width="22" height="22"><use href="#rc-link"/></svg><svg width="22" height="22"><use href="#rc-rows"/></svg></div>
    <div class="cell actions" style="left:600px;gap:4px;color:var(--icon-navy)"><svg width="26" height="26"><use href="#i-edit"/></svg><svg width="24" height="24"><use href="#i-trash"/></svg></div>
  </div>

  <div class="row plain" style="left:479px;top:767px;width:660px;height:31px">
    <span class="cell" style="left:7px">LastModifiedDate</span><span class="cell center" style="left:235px">Common.Last Updated</span>
    <svg class="cell" style="left:379px;color:var(--icon-navy)" width="26" height="26"><use href="#i-check-circle"/></svg>
    <div class="cell rules" style="left:436px;color:var(--icon-navy)"><svg width="22" height="22"><use href="#r-list"/></svg><svg width="22" height="22"><use href="#r-search"/></svg><svg width="22" height="22"><use href="#rc-swap"/></svg><svg width="22" height="22"><use href="#r-dcheck"/></svg><svg width="22" height="22"><use href="#rc-link"/></svg><svg width="22" height="22"><use href="#rc-rows"/></svg></div>
    <div class="cell actions" style="left:600px;gap:4px;color:var(--icon-navy)"><svg width="26" height="26"><use href="#i-edit"/></svg><svg width="24" height="24"><use href="#i-trash"/></svg></div>
  </div>

  <div class="row tint" style="left:479px;top:798px;width:660px;height:31px">
    <span class="cell" style="left:7px">Website</span><span class="cell center" style="left:235px">Organization.Website/URL</span>
    <svg class="cell" style="left:379px;color:var(--icon-navy)" width="26" height="26"><use href="#i-check-circle"/></svg>
    <div class="cell rules" style="left:436px;color:var(--icon-navy)"><svg width="22" height="22"><use href="#rc-list"/></svg><svg width="22" height="22"><use href="#r-search"/></svg><svg width="22" height="22"><use href="#rc-swap"/></svg><svg width="22" height="22"><use href="#rc-dcheck"/></svg><svg width="22" height="22"><use href="#rc-link"/></svg><svg width="22" height="22"><use href="#rc-rows"/></svg></div>
    <div class="cell actions" style="left:600px;gap:4px;color:var(--icon-navy)"><svg width="26" height="26"><use href="#i-edit"/></svg><svg width="24" height="24"><use href="#i-trash"/></svg></div>
  </div>

  <footer class="table-footer">
    <div class="pager">
      <span>«</span><span>‹</span><span class="page-num">1</span><span>›</span><span>»</span>
    </div>
    <span class="record-count">3 of 3 records</span>
    <span class="page-size">20 ⌄</span>
  </footer>
</main>
</body>
</html>
```